I need a flyer designed for a marine service company. Our company specializes in boat engine diagnostic/repair, engine service, electronic installation and repairs, bottom paint, detailing, winterization and shrink wrapping. We would like to see designs that incorporate our color scheme of deep blue, blueish gray and black (please see attached photo)

Target Market(s)

Boat owners

Industry/Entity Type

Marine

Logo Text

Kelpwick Harbor Marine Services

Requirements
Must have
• Company logo
Nice to have
• List the services we provide.

```html
<!DOCTYPE html>
<html lang="en">
<head>
<meta charset="utf-8">
<title>Kelpwick Harbor Marine Services – Flyer</title>
<link href="https://fonts.googleapis.com/css2?family=Montserrat:ital,wght@0,300;0,400;0,500;0,600;0,700;0,800;0,900;1,600;1,700&display=swap" rel="stylesheet">
<style>
  :root {
    --navy: #1c2a58;
    --navy-deep: #19254a;
    --panel-top: #41608f;
    --panel-bottom: #1d2a4f;
    --accent-sky: #84d2e8;
    --signal-yellow: #ece51e;
    --paper: #ffffff;
    --stage: #e9e9e9;
    --ink-soft: #2a2f3a;
  }
  * { margin: 0; padding: 0; box-sizing: border-box; }
  html, body {
    width: 1065px; height: 1200px; overflow: hidden;
    background: var(--stage);
    font-family: "Montserrat", Arial, sans-serif;
  }
  .flyer {
    position: absolute; left: 65px; top: 0;
    width: 934px; height: 1200px;
    background: var(--paper);
    overflow: hidden;
  }
  .flyer-shapes { position: absolute; inset: 0; }

  .brand {
    position: absolute; left: 55px; top: 120px; width: 220px;
    text-align: center; color: var(--navy); font-weight: 500;
  }
  .brand-name { font-size: 21px; letter-spacing: 1px; line-height: 1.2; }
  .brand-sub { font-size: 11px; letter-spacing: 2.5px; margin-top: 6px; }

  .tagline {
    position: absolute; left: 366px; top: 124px;
    color: var(--paper); font-size: 30px; font-weight: 600; font-style: italic;
    letter-spacing: 0.2px;
  }

  .headline {
    position: absolute; left: 51px; top: 296px;
    color: var(--navy); font-size: 45px; font-weight: 900;
    line-height: 48px; letter-spacing: -0.5px;
  }
  .intro {
    position: absolute; left: 51px; top: 403px;
    color: var(--ink-soft); font-size: 17.5px; font-weight: 400; line-height: 27px;
  }

  .emergency {
    position: absolute; left: 650px; top: 399px; width: 194px; height: 194px;
    display: flex; flex-direction: column; align-items: center; justify-content: center;
    color: var(--navy); font-weight: 900; text-align: center; line-height: 1;
  }
  .emergency-num { font-size: 64px; letter-spacing: -1px; }
  .emergency-hour { font-size: 32px; margin-top: -2px; }
  .emergency-text { font-size: 19.5px; margin-top: 2px; }

  .services-title {
    position: absolute; left: 51px; top: 738px;
    color: var(--paper); font-size: 40px; font-weight: 900; letter-spacing: 0.3px;
  }
  .services-list {
    position: absolute; left: 55px; top: 795px; list-style: none;
    color: var(--paper); font-size: 16.5px; font-weight: 600; letter-spacing: 0.2px;
  }
  .services-list li { height: 34.4px; display: flex; align-items: center; }
  .services-list li::before {
    content: ""; width: 0; height: 0; margin-right: 9px;
    border-left: 9px solid var(--signal-yellow);
    border-top: 5.5px solid transparent; border-bottom: 5.5px solid transparent;
  }

  .compare-label {
    position: absolute; color: var(--navy);
    font-size: 12.5px; font-weight: 700; font-style: italic; letter-spacing: 0.4px;
  }

  .call-block { position: absolute; left: 50px; top: 1090px; display: flex; align-items: center; }
  .call-icon { width: 68px; height: 68px; margin-right: 13px; }
  .call-lead { color: var(--navy); font-size: 29px; font-weight: 300; line-height: 1; }
  .call-number { color: var(--navy); font-size: 38px; font-weight: 800; line-height: 1; margin-top: 8px; letter-spacing: 0.3px; }

  .info {
    position: absolute; left: 590px; top: 1078px; color: var(--paper);
  }
  .info-title { font-size: 17.5px; font-weight: 700; letter-spacing: 0.3px; margin-bottom: 12px; }
  .info-row { display: flex; align-items: center; font-size: 15.5px; font-weight: 400; height: 33px; letter-spacing: 0.2px; }
  .info-icon { width: 14px; height: 14px; margin-right: 8px; flex: none; }
</style>
</head>
<body>
<main class="flyer">
  <svg class="flyer-shapes" width="934" height="1200" viewBox="0 0 934 1200" aria-hidden="false">
    <defs>
      <linearGradient id="seaFade" x1="0" y1="0" x2="1" y2="0">
        <stop offset="0" stop-color="#ffffff"/>
        <stop offset="0.3" stop-color="#ffffff"/>
        <stop offset="0.55" stop-color="#d4e3ee"/>
        <stop offset="0.8" stop-color="#9fbdd6"/>
        <stop offset="1" stop-color="#6f93bb"/>
      </linearGradient>
      <linearGradient id="panelFill" x1="0" y1="0" x2="0.35" y2="1">
        <stop offset="0" stop-color="var(--panel-top)"/>
        <stop offset="1" stop-color="var(--panel-bottom)"/>
      </linearGradient>
      <linearGradient id="bannerFill" x1="0" y1="0" x2="1" y2="0">
        <stop offset="0" stop-color="#3f5c8c"/>
        <stop offset="1" stop-color="#1a2549"/>
      </linearGradient>
      <linearGradient id="coveredBoat" x1="0" y1="0" x2="0" y2="1">
        <stop offset="0" stop-color="#7b6a3e"/>
        <stop offset="0.3" stop-color="#e7e8ea"/>
        <stop offset="0.75" stop-color="#d6d8dc"/>
        <stop offset="1" stop-color="#6f6a62"/>
      </linearGradient>
      <linearGradient id="grimyHull" x1="0" y1="0" x2="0" y2="1">
        <stop offset="0" stop-color="#d8cfbb"/>
        <stop offset="1" stop-color="#3c3a35"/>
      </linearGradient>
      <linearGradient id="cleanHull" x1="0" y1="0" x2="0" y2="1">
        <stop offset="0" stop-color="#efe8d6"/>
        <stop offset="1" stop-color="#3a3d44"/>
      </linearGradient>
      <linearGradient id="grimyDeck" x1="0" y1="0" x2="0" y2="1">
        <stop offset="0" stop-color="#c9d3dc"/>
        <stop offset="1" stop-color="#8d8576"/>
      </linearGradient>
      <linearGradient id="cleanDeck" x1="0" y1="0" x2="0" y2="1">
        <stop offset="0" stop-color="#dfe4e8"/>
        <stop offset="1" stop-color="#efe6cf"/>
      </linearGradient>
    </defs>

    <g role="img" aria-label="Photo: bow rail of a white motorboat looking out over open blue water">
      <rect x="0" y="0" width="934" height="700" fill="url(#seaFade)"/>
    </g>

    <polygon points="344,113 821,113 797,172 316,172" fill="url(#bannerFill)"/>

    <polygon points="0,695 367,695 423,569 934,453 934,1200 0,1200" fill="url(#panelFill)"/>

    <polygon points="0,686 360,686 424,497 436,497 372,697 0,697" fill="var(--accent-sky)"/>
    <g role="img" aria-label="Photo: shrink-wrapped boat on a trailer in front of autumn trees">
      <polygon points="0,492 429,492 364,687 0,687" fill="url(#coveredBoat)"/>
    </g>

    <circle cx="747" cy="496" r="97" fill="var(--signal-yellow)"/>

    <polygon points="512,633 712,633 708,644 524,644 470,802 458,802" fill="var(--accent-sky)"/>
    <polygon points="524,642 936,642 936,813 463,813" fill="var(--paper)"/>
    <g role="img" aria-label="Photo before service: dirty transom and outboard engine">
      <polygon points="527,646 756,646 713,809 469,809" fill="url(#grimyHull)"/>
    </g>
    <g role="img" aria-label="Photo after service: cleaned transom and outboard engine">
      <polygon points="761,646 934,646 934,809 718,809" fill="url(#cleanHull)"/>
    </g>
    <polygon points="475,789 553,789 546,809 469,809" fill="var(--signal-yellow)"/>
    <polygon points="719,789 786,789 779,809 713,809" fill="var(--signal-yellow)"/>

    <polygon points="512,860 520,860 466,1017 652,1017 646,1026 456,1026" fill="var(--accent-sky)"/>
    <polygon points="522,847 936,847 936,1019 467,1019" fill="var(--paper)"/>
    <g role="img" aria-label="Photo before detailing: stained deck console">
      <polygon points="525,851 756,851 704,1015 471,1015" fill="url(#grimyDeck)"/>
    </g>
    <g role="img" aria-label="Photo after detailing: clean, polished deck console">
      <polygon points="761,851 934,851 934,1015 709,1015" fill="url(#cleanDeck)"/>
    </g>
    <polygon points="476,995 553,995 546,1015 469,1015" fill="var(--signal-yellow)"/>
    <polygon points="715,995 782,995 775,1015 709,1015" fill="var(--signal-yellow)"/>

    <path d="M0 1059 H405 C468 1059 498 1085 518 1128 L552 1200 H0 Z" fill="var(--signal-yellow)"/>
  </svg>

  <div class="brand">
    <div class="brand-name">KELPWICK HARBOR</div>
    <div class="brand-sub">MARINE SERVICES</div>
  </div>

  <p class="tagline">Fast, Expert &amp; Reliable</p>

  <h1 class="headline">FULL MOBILE<br>MARINE SERVICE</h1>
  <p class="intro">Capable of servicing all makes and<br>models of inboard and outboard vessels.</p>

  <div class="emergency">
    <span class="emergency-num">24</span>
    <span class="emergency-hour">HOUR</span>
    <span class="emergency-text">EMERGENCY</span>
    <span class="emergency-text">CALL</span>
  </div>

  <h2 class="services-title">OUR SERVICES</h2>
  <ul class="services-list">
    <li>BOAT ENGINE DIAGNOSTIC/REPAIR</li>
    <li>ENGINE SERVICE</li>
    <li>ELECTRONIC INSTALLATION AND REPAIRS</li>
    <li>BOTTOM PAINT</li>
    <li>DETAILING</li>
    <li>WINTERIZATION</li>
    <li>SHRINK WRAPPING</li>
  </ul>

  <span class="compare-label" style="left:483px; top:791px;">BEFORE</span>
  <span class="compare-label" style="left:724px; top:791px;">AFTER</span>
  <span class="compare-label" style="left:483px; top:997px;">BEFORE</span>
  <span class="compare-label" style="left:720px; top:997px;">AFTER</span>

  <div class="call-block">
    <svg class="call-icon" viewBox="0 0 68 68" aria-hidden="true">
      <circle cx="34" cy="34" r="31.5" fill="none" stroke="var(--navy)" stroke-width="3"/>
      <path d="M27 17 h6 l2 10 -5 3 c0 5 0 9 0 8 l5 3 -2 10 h-6 c-5 -4 -7 -10 -7 -17 s2 -13 7 -17 z" fill="none" stroke="var(--navy)" stroke-width="3" stroke-linejoin="round"/>
    </svg>
    <div>
      <div class="call-lead">CALL US TODAY!</div>
      <div class="call-number">+1 555-014-2290</div>
    </div>
  </div>

  <div class="info">
    <div class="info-title">FOR MORE INFORMATION</div>
    <div class="info-row">
      <svg class="info-icon" viewBox="0 0 14 14" aria-hidden="true">
        <rect x="0.5" y="2.5" width="13" height="9" rx="1" fill="var(--paper)"/>
        <path d="M1 3.5 L7 8 L13 3.5" fill="none" stroke="var(--navy-deep)" stroke-width="1.3"/>
      </svg>
      hello@kelpwickharbor.net
    </div>
    <div class="info-row">
      <svg class="info-icon" viewBox="0 0 14 14" aria-hidden="true">
        <rect x="1" y="1" width="12" height="12" fill="var(--paper)"/>
      </svg>
      @KelpwickHarborMarineServices
    </div>
  </div>
</main>
</body>
</html>
```